Brochure Design Project

WE NEED A BROCHURE!!! - This should be easy and allows you to be creative! Plumtree Orbit creates web and mobile portals for businesses in the health and wellness industry. The websites and mobile apps engage our clients' patients and consumers in health and wellness activities such as managing their conditions or losing weight. We leverage our large platform code-stack to build custom solutions for each client. We really love our website www.plumtreeorbit-example.com. So all we need is for someone to take that branding and create a 2-4 page brochure. The text is not that important as we can change it as needed. Mostly we just need the layout. We'd like to include the Sun Ray Hub colors and the JOURNAL font as included on our website.

Industry/Entity Type

Health

Requirements
Must have
• The 2 PDFs uploaded are 2 attempts that we aren't happy with but can be used as a reference only. Please be creative.

Must have the same branding language as our website www.plumtreeorbit-example.com - so that it looks like the same company.

Must have format/room for images. You can plug in stock photography if you'd like and we can buy or add in custom images later.

The font is JOURNAL for the sun/ray/hub. Other fonts are optional. Colors are:

Me – Green RGB 140, 188, 0
We – Blue RGB 11, 116, 187
Info – Orange RGB 237, 137, 33
Dark Gray – RGB 70, 80, 89
Med Gray – 114, 132, 154
Light Gray – 236, 238, 239

Thank you!

```html
<!DOCTYPE html>
<html lang="en">
<head>
<meta charset="utf-8">
<title>Plumtree Orbit – Brochure layout, cover and back pages</title>
<link rel="stylesheet" href="https://fonts.googleapis.com/css2?family=Open+Sans:ital,wght@0,400;0,600;0,700;1,400;1,600;1,700&family=PT+Sans:wght@700&display=swap">
<style>
  :root {
    --green: rgb(140, 188, 0);
    --blue: rgb(11, 116, 187);
    --orange: rgb(237, 137, 33);
    --dark-gray: rgb(70, 80, 89);
    --logo-gray: #3b4650;
    --med-gray: rgb(114, 132, 154);
    --light-gray: rgb(236, 238, 239);
    --band-gray: #f1f2f3;
    --label-gray: #c4c8cc;
    --board-top: #e6e8ea;
    --board-bottom: #ffffff;
    --paper: #ffffff;
  }
  * { box-sizing: border-box; margin: 0; padding: 0; }
  html, body { width: 1200px; height: 900px; overflow: hidden; }
  body {
    position: relative;
    background: linear-gradient(to bottom, var(--board-top) 0%, #f3f4f5 60%, var(--board-bottom) 100%);
    font-family: "Open Sans", Arial, sans-serif;
    color: var(--dark-gray);
  }
  .page {
    position: absolute;
    background: var(--paper);
    box-shadow: 0 4px 10px rgba(0,0,0,0.18);
    overflow: hidden;
  }
  .page-cover { left: 52px; top: 52px; width: 533px; height: 690px; }
  .page-back { left: 655px; top: 100px; width: 498px; height: 645px; }
  .page-shapes { position: absolute; inset: 0; width: 100%; height: 100%; }
  .page-shapes polygon { fill: var(--band-gray); }
  .page-fold {
    position: absolute; top: 0; bottom: 0; width: 22px;
    background: linear-gradient(to right, rgba(0,0,0,0.07), rgba(0,0,0,0));
  }
  .page-fold-left { left: 0; }
  .page-fold-right { right: 0; transform: scaleX(-1); }

  .brand-name {
    position: absolute;
    font-family: "PT Sans", Arial, sans-serif;
    font-weight: 700;
    color: var(--logo-gray);
    letter-spacing: -0.5px;
    white-space: nowrap;
  }
  .brand-tagline {
    position: absolute;
    font-weight: 400;
    color: var(--dark-gray);
    white-space: nowrap;
  }
  .hub-name {
    position: absolute;
    font-family: "PT Sans", Arial, sans-serif;
    font-weight: 700;
    color: var(--green);
    white-space: nowrap;
  }

  .cover-brand { left: 36px; top: 176px; font-size: 42px; }
  .cover-tagline { left: 36px; top: 232px; font-size: 17px; }
  .cover-hub { left: 40px; top: 574px; font-size: 30px; }
  .cover-photo {
    position: absolute; left: 333px; top: 103px; width: 200px; height: 453px;
    background: linear-gradient(160deg, #dcdcdc 0%, #b9b9b9 35%, #e4e4e4 60%, #f2f2f2 100%);
  }

  .back-hub { right: 40px; top: 60px; font-size: 27px; }
  .back-brand { left: 74px; top: 196px; font-size: 32px; }
  .back-tagline { left: 74px; top: 238px; font-size: 14.5px; }

  .office { position: absolute; top: 511px; font-size: 8px; line-height: 11px; color: var(--dark-gray); }
  .office-head { left: 87px; }
  .office-intl { left: 302px; }
  .office-title { font-style: italic; font-weight: 600; margin-bottom: 7px; }
  .office-name { font-weight: 700; position: relative; padding-left: 9px; }
  .office-name::before {
    content: ""; position: absolute; left: 0; top: 4px; width: 3px; height: 3px;
    border-radius: 50%; background: var(--green);
  }
  .office-lines { padding-left: 9px; margin-top: 1px; }
  .office-lines b { font-style: italic; }

  .back-footer {
    position: absolute; left: 0; right: 0; bottom: 0; height: 40px;
    display: flex; align-items: center; justify-content: space-between;
    padding: 0 22px 0 87px; font-size: 9px; font-weight: 700; color: var(--dark-gray);
  }
  .back-footer .demo { font-weight: 700; }
  .back-footer .demo span { font-weight: 400; }
  .back-footer .divider { display: inline-block; width: 1px; height: 11px; background: var(--med-gray); margin: 0 8px; vertical-align: middle; }
  .back-footer .mail { font-style: italic; }

  .board-label { position: absolute; top: 764px; font-size: 19px; color: var(--label-gray); }
  .label-cover { left: 52px; }
  .label-back { left: 652px; }

  .board-caption { position: absolute; top: 836px; left: 50px; display: flex; align-items: baseline; white-space: nowrap; }
  .caption-brand { font-family: "PT Sans", Arial, sans-serif; font-weight: 700; font-size: 24px; color: #b3b7bb; margin-right: 34px; }
  .caption-text { font-size: 20px; color: #b6babe; letter-spacing: 0.5px; font-weight: 600; }
  .caption-text span { font-weight: 400; }
  .caption-number { font-size: 32px; font-weight: 600; color: #b3b7bb; margin-left: 24px; }
</style>
</head>
<body>

  <section class="page page-cover" aria-label="Brochure cover page">
    <svg class="page-shapes" viewBox="0 0 533 690" preserveAspectRatio="none" aria-hidden="true">
      <polygon points="0,0 252,0 224,133 0,133"/>
      <polygon points="362,0 533,0 533,55 350,55"/>
      <polygon points="0,300 533,300 533,528 0,528"/>
      <polygon points="330,612 533,612 533,690 312,690"/>
    </svg>
    <div class="cover-photo" role="img" aria-label="Black and white photo of a smiling senior doctor with glasses and a stethoscope"></div>
    <div class="brand-name cover-brand">Plumtree Orbit</div>
    <div class="brand-tagline cover-tagline">Healthy Customer Portals</div>
    <div class="hub-name cover-hub">Sun Ray Hub</div>
    <div class="page-fold page-fold-left"></div>
  </section>

  <section class="page page-back" aria-label="Brochure back page">
    <svg class="page-shapes" viewBox="0 0 498 645" preserveAspectRatio="none" aria-hidden="true">
      <polygon points="0,0 270,0 246,122 0,122"/>
      <polygon points="336,150 498,150 498,295 306,295"/>
      <polygon points="0,295 498,295 498,480 0,480"/>
      <polygon points="0,605 498,605 498,645 0,645"/>
    </svg>
    <div class="hub-name back-hub">Sun Ray Hub</div>
    <div class="brand-name back-brand">Plumtree Orbit</div>
    <div class="brand-tagline back-tagline">Healthy Customer Portals</div>

    <div class="office office-head">
      <p class="office-title">Head Office:</p>
      <p class="office-name">Plumtree Orbit, Inc.</p>
      <p class="office-lines">48 Harbor Lane, Suite 210<br>Linden Falls, NY 10990<br>Phone: (555) <b>014 2238</b> Fax: (555) <b>014 2239</b></p>
    </div>
    <div class="office office-intl">
      <p class="office-title">International R&amp;D Office</p>
      <p class="office-name">Plumtree Orbit</p>
      <p class="office-lines">Cedar Street #12<br>Riverton, Israel<br>Phone: +1 (555) <b>017 4410</b></p>
    </div>

    <div class="back-footer">
      <span class="site">www.plumtreeorbit-example.com</span>
      <span class="demo">For a demo <span>contact</span><i class="divider"></i><span class="mail">info@plumtreeorbit-example.com</span></span>
    </div>
    <div class="page-fold page-fold-right"></div>
  </section>

  <div class="board-label label-cover">cover</div>
  <div class="board-label label-back">back</div>

  <div class="board-caption">
    <span class="caption-brand">Plumtree Orbit</span>
    <span class="caption-text">Brochure layout <span>- cover/back pages</span></span>
    <span class="caption-number">1</span>
  </div>

</body>
</html>
```